Retractable Banner Design featuring Key Product for Beauty Trade Show (Eyelash Extensions)

We're a beauty/nail supply company that specializes in products used in professional nail salons. The key product for this design is "Eyelash Extensions".

We will be exhibiting in a trade show and are looking for a free-standing Retractable Banner Design that will be displayed at the front of our booth. The goal of the banner will be to display key products that are high in demand with our customers. The banner will be used to attract attention and highlight key selling points of these popular products. We would like the banner to be focused on the product title, image and key points, with a beauty/model/pattern background to create a professional appearance.

Target Market(s)

Nail Salons

Industry/Entity Type

Beauty

Requirements
Nice to have
• Eyelash model or close up of eyelash product in use.

```html
<!DOCTYPE html>
<html lang="en">
<head>
<meta charset="utf-8">
<title>Lumira Professional – Eyelash Extensions Retractable Banner</title>
<link rel="stylesheet" href="https://fonts.googleapis.com/css2?family=Dosis:wght@500;600&family=Didact+Gothic&display=swap">
<style>
  :root {
    --canvas-bg: #ffffff;
    --ink-black: #0b0b0b;
    --gold: #d9c68c;
    --white: #ffffff;
    --tray-light: #e9e9e9;
    --tray-mid: #bdbdbd;
    --photo-top: #5f5f5f;
    --photo-mid: #c9c9c9;
    --photo-low: #6a6a6a;
    --photo-bottom: #000000;
  }
  * { margin: 0; padding: 0; box-sizing: border-box; }
  html, body {
    width: 1200px;
    height: 1200px;
    overflow: hidden;
    background: var(--canvas-bg);
  }
  .banner {
    position: absolute;
    left: 369px;
    top: 100px;
    width: 462px;
    height: 1000px;
    overflow: hidden;
    color: var(--white);
    font-family: "Didact Gothic", "Century Gothic", sans-serif;
  }
  .banner__photo {
    position: absolute;
    inset: 0;
    background:
      radial-gradient(ellipse 55% 14% at 42% 22%, rgba(20,20,20,0.75), rgba(20,20,20,0) 70%),
      linear-gradient(180deg,
        var(--photo-top) 0%,
        #9a9a9a 12%,
        #b4b4b4 24%,
        var(--photo-mid) 40%,
        #a9a9a9 52%,
        var(--photo-low) 64%,
        #2a2a2a 78%,
        var(--photo-bottom) 90%);
  }
  .brand {
    position: absolute;
    left: 0;
    right: 0;
    top: 300px;
    text-align: center;
    color: var(--ink-black);
    font-family: "Dosis", sans-serif;
    font-weight: 600;
  }
  .brand__name {
    display: block;
    font-size: 84px;
    line-height: 1;
    letter-spacing: -1px;
  }
  .brand__descriptor {
    display: block;
    font-size: 20px;
    line-height: 1;
    margin-top: 4px;
    padding-left: 190px;
  }
  .headline {
    position: absolute;
    left: 0;
    right: 0;
    top: 440px;
    text-align: center;
    font-family: "Dosis", sans-serif;
    font-weight: 600;
    font-size: 46px;
    line-height: 1;
    color: var(--gold);
  }
  .tray {
    position: absolute;
    left: 26px;
    width: 152px;
    border-radius: 4px;
    background:
      repeating-linear-gradient(180deg,
        rgba(40,40,40,0.55) 0 8px,
        rgba(40,40,40,0) 8px 26px),
      linear-gradient(180deg, var(--tray-light), var(--tray-mid));
  }
  .tray--falsies { top: 520px; height: 107px; }
  .tray--long { top: 647px; height: 104px; }
  .tray--flares { top: 772px; height: 106px; }
  .feature {
    position: absolute;
    left: 206px;
    width: 250px;
  }
  .feature__title {
    font-family: "Dosis", sans-serif;
    font-weight: 600;
    font-size: 23px;
    line-height: 1.1;
    color: var(--gold);
  }
  .feature__text {
    font-size: 17px;
    line-height: 21.5px;
    color: var(--white);
  }
  .feature--falsies { top: 508px; }
  .feature--long { top: 602px; }
  .feature--handmade { top: 696px; }
  .feature--flares { top: 791px; }
  .quantity {
    position: absolute;
    left: 57px;
    top: 898px;
    font-size: 17px;
    color: var(--white);
  }
  .quantity__label {
    font-family: "Dosis", sans-serif;
    font-weight: 600;
  }
</style>
</head>
<body>
  <main class="banner">
    <div class="banner__photo" role="img" aria-label="Black and white close-up of a closed eye with long lash extensions, fading to black toward the bottom"></div>

    <div class="brand">
      <span class="brand__name">Lumira</span>
      <span class="brand__descriptor">Professional</span>
    </div>

    <h1 class="headline">Eyelash Extensions</h1>

    <div class="tray tray--falsies" role="img" aria-label="Tray of knot-free flare lashes, medium black"></div>
    <div class="tray tray--long" role="img" aria-label="Tray of 12-ply knot-free flare lashes"></div>
    <div class="tray tray--flares" role="img" aria-label="Tray of triple 15-ply flare lashes"></div>

    <section class="feature feature--falsies">
      <h2 class="feature__title">Professional Falsies</h2>
      <p class="feature__text">Create beautiful and<br>eye-opening appearances</p>
    </section>
    <section class="feature feature--long">
      <h2 class="feature__title">Long-Lasting</h2>
      <p class="feature__text">Delicate overlapping hairs<br>create the most authentic look</p>
    </section>
    <section class="feature feature--handmade">
      <h2 class="feature__title">Handmade Perfection</h2>
      <p class="feature__text">Individually hand made with<br>extreme attention to detail</p>
    </section>
    <section class="feature feature--flares">
      <h2 class="feature__title">Knot-Free Flares</h2>
      <p class="feature__text">Each tray holds 56 individual<br>flares with a dramatic C-Curl</p>
    </section>

    <p class="quantity"><span class="quantity__label">Quantity:</span> (100 Trays/Box), (12 Boxes/Case)</p>
  </main>
</body>
</html>
```